Become a Mentor - For Musicians, Artists, Producers and Teachers

Here is the full creative brief:

https://sheets.plorvex.com/grids/d/9kTmWqRz4_PLbN2sYhC8vXeJ3uKdAfG7nLoQwErTpMzb/view?src=shared

Here is the background image file: https://www.filquarry.com/fs/83tbwmynq4kpz/BBLs7h2QNF8PcTwXX-mk3RUVb?get=0

LOGO:
https://www.filquarry.com/fs/w472mujakd8n5/BBCK6TueRP3Z-hVLwYnZ1Xbba?get=0

```html
<!DOCTYPE html>
<html lang="en">
<head>
<meta charset="utf-8">
<title>Become a Mentor – Ad Set</title>
<link rel="stylesheet" href="https://fonts.googleapis.com/css2?family=Saira+Semi+Condensed:wght@600;700&family=Kaushan+Script&display=swap">
<style>
:root{
  --sky:#2fa8e0;
  --sky-text:#35a9e1;
  --amber:#efa84c;
  --ink:#050505;
  --paper:#ffffff;
  --studio-a:#6b5d52;
  --studio-b:#3a3634;
  --studio-c:#8a8580;
}
*{margin:0;padding:0;box-sizing:border-box}
html,body{width:1200px;height:917px;overflow:hidden;background:var(--paper)}
body{position:relative;font-family:"Saira Semi Condensed","Arial Narrow",Arial,sans-serif;font-weight:700;color:var(--paper)}
.ad{position:absolute;background:var(--ink);overflow:hidden}
.ad > *{position:absolute}
.ad--portrait{left:32px;top:31px;width:605px;height:849px}
.ad--square{left:663px;top:34px;width:512px;height:512px}
.ad--banner{left:663px;top:571px;width:512px;height:190px}

.photo{background:linear-gradient(100deg,var(--studio-c) 0%,var(--studio-a) 35%,var(--studio-b) 70%,#4c4a4a 100%)}
.photo-fade{background:linear-gradient(to bottom,rgba(5,5,5,0) 0%,rgba(5,5,5,0) 55%,var(--ink) 100%)}
.band{background:var(--sky);display:flex;justify-content:center;align-items:center;color:var(--paper);text-transform:uppercase;white-space:nowrap}
.script{font-family:"Kaushan Script",cursive;font-weight:400;color:var(--paper);line-height:1;white-space:nowrap}
.apply{background:var(--amber);display:flex;flex-direction:column;justify-content:center;align-items:flex-end;line-height:1.05;text-transform:uppercase}
.apply span:first-child{color:var(--paper)}
.apply span:last-child{color:var(--ink)}
.headline{color:var(--sky-text);text-transform:uppercase;line-height:1.15;white-space:nowrap}
.audience{color:var(--amber);text-transform:uppercase;line-height:1.2;white-space:nowrap}
.contact{display:flex;align-items:center;color:var(--paper);text-transform:uppercase;white-space:nowrap;font-weight:600}
.contact svg{flex:none;color:var(--sky-text)}
.brand{display:flex;align-items:center;gap:8px;color:var(--paper);text-transform:uppercase;line-height:1.1;white-space:nowrap}
.brand-dot{flex:none;border-radius:50%;background:var(--sky)}
</style>
</head>
<body>
<svg width="0" height="0" style="position:absolute" aria-hidden="true">
  <defs>
    <symbol id="icon-phone" viewBox="0 0 24 24"><circle cx="12" cy="12" r="11" fill="none" stroke="currentColor" stroke-width="1.6"/><path d="M8.6 6.8l1.8-.4 1 2.6-1.2.9a7 7 0 0 0 3.9 3.9l.9-1.2 2.6 1-.4 1.8c-.2.6-.8 1-1.4.9A9.5 9.5 0 0 1 7.7 8.2c-.1-.6.3-1.2.9-1.4z" fill="currentColor"/></symbol>
    <symbol id="icon-mail" viewBox="0 0 24 24"><circle cx="12" cy="12" r="11" fill="none" stroke="currentColor" stroke-width="1.6"/><rect x="6.5" y="8" width="11" height="8" fill="none" stroke="currentColor" stroke-width="1.4"/><path d="M6.5 8l5.5 4.5L17.5 8" fill="none" stroke="currentColor" stroke-width="1.4"/></symbol>
    <symbol id="icon-web" viewBox="0 0 24 24"><circle cx="12" cy="12" r="11" fill="none" stroke="currentColor" stroke-width="1.6"/><circle cx="12" cy="12" r="6" fill="none" stroke="currentColor" stroke-width="1.3"/><path d="M6 12h12M12 6c-2.2 2.4-2.2 9.6 0 12M12 6c2.2 2.4 2.2 9.6 0 12" fill="none" stroke="currentColor" stroke-width="1.1"/></symbol>
  </defs>
</svg>

<!-- Portrait poster -->
<section class="ad ad--portrait">
  <div class="photo" role="img" aria-label="Photo of two young musicians talking in a recording studio beside a mixing desk and speakers" style="left:0;top:125px;width:605px;height:460px"></div>
  <div class="photo-fade" style="left:0;top:125px;width:605px;height:460px"></div>
  <div class="band" style="left:0;top:0;width:605px;height:150px;font-size:49px;padding-bottom:18px;clip-path:polygon(0 0,100% 0,100% 84%,92% 86%,84% 83%,74% 87%,63% 84%,52% 88%,41% 85%,30% 89%,19% 86%,9% 90%,0 87%)">Start Your Career</div>
  <div class="apply" style="left:430px;top:436px;width:175px;height:112px;padding-right:26px;font-size:36px;clip-path:polygon(4% 6%,30% 0,62% 4%,100% 1%,100% 100%,70% 96%,35% 100%,6% 95%,0 60%,3% 30%)"><span>Apply</span><span>Now</span></div>
  <div class="script" style="left:95px;top:388px;font-size:52px">Become a</div>
  <div class="script" style="left:18px;top:456px;font-size:70px">Mentor Today</div>
  <div class="headline" style="left:22px;top:592px;font-size:31px">Turn your skills and passion<br>for music into a career</div>
  <div class="audience" style="left:22px;top:697px;font-size:17px">Designed for musicians, artists, producers &amp; teachers</div>
  <div class="contact" style="left:20px;top:743px;font-size:13px;gap:18px"><svg width="24" height="24"><use href="#icon-phone"/></svg>Call 1300 XXX XXX</div>
  <div class="contact" style="left:20px;top:783px;font-size:13px;gap:18px"><svg width="24" height="24"><use href="#icon-mail"/></svg>youremail@meridianacademyofsound.com.au</div>
  <div class="contact" style="left:20px;top:823px;font-size:13px;gap:18px"><svg width="24" height="24"><use href="#icon-web"/></svg>www.meridianacademyofsound.com.au</div>
  <div class="brand" style="left:470px;top:768px;font-size:13px"><span class="brand-dot" style="width:16px;height:16px"></span><span>Meridian<br>Academy<br>of Sound</span></div>
</section>

<!-- Square tile -->
<section class="ad ad--square">
  <div class="photo" role="img" aria-label="Photo of two young musicians talking in a recording studio beside a mixing desk and speakers" style="left:0;top:70px;width:512px;height:285px"></div>
  <div class="photo-fade" style="left:0;top:70px;width:512px;height:285px"></div>
  <div class="band" style="left:0;top:0;width:512px;height:84px;font-size:38px;padding-bottom:8px;clip-path:polygon(0 0,100% 0,100% 88%,88% 91%,75% 87%,62% 92%,48% 88%,34% 93%,20% 89%,8% 94%,0 90%)">Start Your Career</div>
  <div class="apply" style="left:408px;top:290px;width:104px;height:76px;padding-right:12px;font-size:24px;clip-path:polygon(5% 6%,40% 0,100% 3%,100% 100%,50% 96%,6% 100%,0 55%)"><span>Apply</span><span>Now</span></div>
  <div class="script" style="left:78px;top:222px;font-size:42px">Become a</div>
  <div class="script" style="left:18px;top:270px;font-size:56px">Mentor Today</div>
  <div class="headline" style="left:14px;top:364px;font-size:22px">Turn your skills and passion<br>for music into a career</div>
  <div class="audience" style="left:14px;top:425px;font-size:13.5px">Designed for musicians, artists, producers &amp; teachers</div>
  <div class="contact" style="left:12px;top:450px;font-size:10px;gap:9px"><svg width="14" height="14"><use href="#icon-phone"/></svg>Call 1300 XXX XXX</div>
  <div class="contact" style="left:12px;top:471px;font-size:10px;gap:9px"><svg width="14" height="14"><use href="#icon-mail"/></svg>youremail@meridianacademyofsound.com.au</div>
  <div class="contact" style="left:12px;top:492px;font-size:10px;gap:9px"><svg width="14" height="14"><use href="#icon-web"/></svg>www.meridianacademyofsound.com.au</div>
  <div class="brand" style="left:408px;top:458px;font-size:10px;gap:6px"><span class="brand-dot" style="width:11px;height:11px"></span><span>Meridian<br>Academy<br>of Sound</span></div>
</section>

<!-- Wide banner -->
<section class="ad ad--banner">
  <div class="photo" role="img" aria-label="Photo of two young musicians talking in a recording studio beside a mixing desk and speakers" style="left:0;top:0;width:302px;height:190px"></div>
  <div class="band" style="left:280px;top:0;width:232px;height:52px;font-size:18px;clip-path:polygon(0 0,100% 0,100% 92%,0 68%)"><span style="display:block;transform:rotate(4deg) translateY(-4px)">Start Your Career</span></div>
  <div class="apply" style="left:242px;top:132px;width:64px;height:46px;padding-right:7px;font-size:14px;clip-path:polygon(5% 6%,50% 0,100% 4%,100% 100%,40% 96%,4% 100%,0 55%)"><span>Apply</span><span>Now</span></div>
  <div class="script" style="left:40px;top:84px;font-size:30px">Become a</div>
  <div class="script" style="left:10px;top:114px;font-size:40px">Mentor Today</div>
  <div class="headline" style="left:310px;top:62px;font-size:10px">Turn your skills and passion<br>for music into a career</div>
  <div class="audience" style="left:310px;top:92px;font-size:9.5px;line-height:1.15">Designed for musicians, artists,<br>producers &amp; teachers</div>
  <div class="contact" style="left:310px;top:134px;font-size:7px;gap:5px"><svg width="10" height="10"><use href="#icon-phone"/></svg>Call 1300 XXX XXX</div>
  <div class="contact" style="left:310px;top:152px;font-size:7px;gap:5px"><svg width="10" height="10"><use href="#icon-mail"/></svg>youremail@meridianacademyofsound.com.au</div>
  <div class="contact" style="left:310px;top:170px;font-size:7px;gap:5px"><svg width="10" height="10"><use href="#icon-web"/></svg>www.meridianacademyofsound.com.au</div>
</section>
</body>
</html>
```